Business Card Design Project

We would like you to create business cards. The color scheme should match our website and logo. I have attached an image of a page of our website, as well as our logo. Please Please include the logo on the left with a similar faded horizontal line, and a blueprint type sketch of a house on cribbing on the right, similar to our website. We like the idea of how this looks. I have attached a third image of an actual house on cribbing (crisscrossed wooden beams). Please include cribbing in the blueprint type sketch.

The information to be included on the business cards is

(name)
214 Alder Lane
Suite 317
Fairbrook, NJ 07491
908.641.2093
www.brickwardliftworks.com
info@brickwardliftworks.com

This information can be spaced in any way.

I will also be posting a job for letterhead using the same design as the business cards.

If you need anything other information or I have not been clear enough, please do not hesitate to message me.

Thank you!
Updates

This design project is now open to all designers.  Please message me with any questions.  Thank you.

Industry/Entity Type

House

Requirements
Must have
• 1. Our logo
2. Blueprint type sketch of a house on wooden cribbing.
3. Color scheme to match logo and website.
4. Information provided.

```html
<!DOCTYPE html>
<html lang="en">
<head>
<meta charset="utf-8">
<title>Brickward Liftworks – Business Cards</title>
<link rel="stylesheet" href="https://fonts.googleapis.com/css2?family=Arimo:wght@400;700&display=swap">
<style>
  :root {
    --bg: #e4e4e4;
    --card-light: #f4f3f0;
    --card-dark: #1c1c1d;
    --ink: #1e1e1e;
    --ink-soft: #3a3a3a;
    --orange: #ea8a1c;
    --sketch-a: #e9e9e7;
    --sketch-b: #cfcfcd;
    --pennant: #f2f1ee;
  }
  * { margin: 0; padding: 0; box-sizing: border-box; }
  html, body { width: 1200px; height: 900px; overflow: hidden; }
  body {
    background: var(--bg);
    font-family: "Arimo", Arial, sans-serif;
    position: relative;
  }
  .card {
    position: absolute;
    left: 250px;
    width: 700px;
    height: 400px;
    box-shadow: 0 6px 18px rgba(0,0,0,.25);
    overflow: hidden;
  }
  /* Front */
  .card-front { top: 40px; background: var(--card-light); }
  .house-sketch {
    position: absolute;
    left: 300px; top: 50px;
    width: 370px; height: 300px;
    background: radial-gradient(ellipse at 55% 50%, var(--sketch-b) 0%, var(--sketch-a) 55%, var(--card-light) 85%);
  }
  .brand {
    position: absolute;
    left: 70px; top: 70px;
    display: flex; align-items: center; gap: 10px;
  }
  .brand-mark { display: block; width: 16px; height: 16px; background: var(--orange); }
  .brand-name {
    font-weight: 700; font-size: 24px; color: var(--ink-soft);
    letter-spacing: .5px; text-transform: uppercase;
  }
  .tagline {
    position: absolute; left: 96px; top: 104px;
    font-size: 11px; color: var(--orange);
  }
  .person-name {
    position: absolute; left: 70px; top: 160px;
    font-size: 24px; font-weight: 700; color: var(--orange);
    letter-spacing: .5px;
  }
  .address {
    position: absolute; left: 70px; top: 208px;
    font-size: 17px; line-height: 26px; color: var(--ink);
    list-style: none;
  }
  .contact {
    position: absolute; left: 300px; top: 272px;
    font-size: 16px; line-height: 26px; color: var(--ink);
    list-style: none;
  }
  .contact .strong { font-weight: 700; }
  /* Back */
  .card-back { top: 470px; background: var(--card-dark); }
  .pennant { position: absolute; left: 250px; top: 0; }
  .back-brand {
    position: absolute; left: 250px; top: 80px; width: 230px;
    text-align: center;
  }
  .back-brand .brand-mark { margin: 0 auto 14px; width: 18px; height: 18px; }
  .back-brand .brand-name { font-size: 22px; line-height: 28px; display: block; }
  .back-brand .tagline { position: static; display: block; margin-top: 8px; }
  .back-url {
    position: absolute; left: 0; right: 0; top: 318px;
    text-align: center; font-size: 30px; color: var(--orange);
  }
</style>
</head>
<body>
  <section class="card card-front">
    <div class="house-sketch" role="img" aria-label="Blueprint-style sketch of a two-storey house raised on wooden cribbing"></div>
    <div class="brand">
      <span class="brand-mark"></span>
      <span class="brand-name">Brickward Liftworks</span>
    </div>
    <p class="tagline">House Raising Construction Masonry</p>
    <h1 class="person-name">JORDAN MERCER</h1>
    <ul class="address">
      <li>214 Alder Lane</li>
      <li>Suite 317</li>
      <li>Fairbrook, NJ 07491</li>
    </ul>
    <ul class="contact">
      <li>908.641.2093</li>
      <li><span class="strong">info</span>@brickwardliftworks.com</li>
      <li>www.<span class="strong">brickwardliftworks</span>.com</li>
    </ul>
  </section>

  <section class="card card-back">
    <svg class="pennant" width="230" height="260" viewBox="0 0 230 260" aria-hidden="true">
      <path d="M0 0 H230 V200 L115 250 L0 200 Z" fill="var(--orange)"/>
      <path d="M0 0 H230 V182 L115 228 L0 182 Z" fill="var(--pennant)"/>
      <line x1="8" y1="0" x2="8" y2="180" stroke="var(--orange)" stroke-width="1"/>
      <line x1="222" y1="0" x2="222" y2="180" stroke="var(--orange)" stroke-width="1"/>
    </svg>
    <div class="back-brand">
      <span class="brand-mark"></span>
      <span class="brand-name">Brickward<br>Liftworks</span>
      <span class="tagline">House Raising Construction Masonry</span>
    </div>
    <p class="back-url">www.brickwardliftworks.com</p>
  </section>
</body>
</html>
```